Academic bored with usual scientific poster design needs poster for conference

I need a poster to display the background, aims, process, outcome, next steps and lessons learnt related to the implementation of an electronic documentation project called Clear Ledger. The project involved the replacement of paper based medical record with electronic. The size of the final product needs to be A0 in a portrait orientation. Please see outline of poster content attached. Some of the content is yet to be finalised (as noted in attachment). The successful transition from paper to electronic system is what we want to convey. The logo of the hospital (to be provided) is red so it may be helpful as a starting point for colours. Although the duration is five day i will need to finalise the work on the 25th August for printing and delivery to conference organisers.
Updates

Please note that further attachments have been added - an excel file containing the outcome graph and further explanation in the content docx

Target Market(s)

The target market is a groups of academics with an interest in improved patient care through innovative solutions. It is for display at a conference with a focus on innovation, patient centred care, ...called MERIDA forum 2014 if you want to google it.

Industry/Entity Type

Electronic

Font styles to use
Sans Serif

Requirements
Must have
• The title must be as written in the supporting document -(but it does not have to have to word "title" in front)
The authors and contact also need to appear, but do not need to be very prominent
The organisation logo has to appear - now attached

I will supply graphs for the results section, the results are still being finalised.
Nice to have
• I would like to display as much of the information as graphically as possible, although there still has to be written content given the nature of the project.

A prime example is the method section - this is wordy and bulky in a table at the moment, but I would like to represent this as a timeline graphically somehow, showing the work that has been done over the last three years.
Should not have
• Too much dark background that makes it difficult to read.

```html
<!DOCTYPE html>
<html lang="en">
<head>
<meta charset="utf-8">
<title>Clear Ledger – conference poster</title>
<link rel="stylesheet" href="https://fonts.googleapis.com/css2?family=Exo+2:wght@400;500;600&family=PT+Sans:wght@400;700&display=swap">
<style>
:root{
  --page:#ffffff;
  --field:#0a3e66;
  --panel:#0b5688;
  --title:#1ea6e2;
  --subtitle:#1d4f7e;
  --heading:#f3e35a;
  --subhead:#3fb7ea;
  --text:#ffffff;
  --note:#fbe98c;
  --note-ink:#4a4a3a;
  --green:#8dc63f;
  --orange:#f7941d;
  --grey:#8597a8;
  --yellow:#f3e35a;
  --plum:#8a5a8c;
}
*{box-sizing:border-box;margin:0;padding:0}
html,body{width:857px;height:1200px;overflow:hidden;background:var(--page)}
body{position:relative;font-family:"PT Sans",Arial,sans-serif;color:var(--text)}
.poster-header{position:absolute;left:0;top:0;width:857px;height:150px;background:var(--page)}
.author-note{position:absolute;left:31px;top:42px;width:94px;height:82px;background:var(--note);transform:rotate(-9deg);box-shadow:2px 3px 4px rgba(0,0,0,.25);padding:8px 8px;color:var(--note-ink);font-size:10px;line-height:1.25}
.author-note strong{display:block;color:#2a86c8;font-size:11px;font-weight:700}
.poster-title{position:absolute;left:155px;top:26px;width:668px;text-align:center;font-family:"Exo 2",sans-serif}
.poster-title .name{display:block;color:var(--title);font-size:34px;font-weight:500;letter-spacing:.5px;line-height:40px;padding-left:10px}
.poster-title .line{display:block;color:var(--subtitle);font-size:29.5px;font-weight:400;line-height:36px;text-align:justify;text-align-last:justify}
.field{position:absolute;left:0;top:150px;width:857px;height:1050px;background:var(--field)}
.panel{position:absolute;background:var(--panel)}
.section-title{font-family:"Exo 2",sans-serif;font-size:17px;font-weight:500;color:var(--heading);letter-spacing:.3px}
.section-title small{font-family:"PT Sans",sans-serif;font-size:10px;color:var(--text);letter-spacing:0;margin-left:4px}
.sub{font-family:"Exo 2",sans-serif;color:var(--subhead);font-size:13px;font-weight:500}
p,li{font-size:10.3px;line-height:16px}
ul{list-style:none}
.arrows li{padding-left:18px;position:relative}
.arrows li::before{content:"";position:absolute;left:5px;top:6px;border-left:7px solid var(--text);border-top:3px solid transparent;border-bottom:3px solid transparent}
.arrows li::after{content:"";position:absolute;left:2px;top:8px;width:4px;height:1.5px;background:var(--text)}
.background{left:13px;top:163px;width:487px;height:192px}
.background .section-title{position:absolute;left:8px;top:8px}
.audit{position:absolute;left:8px;top:38px;width:212px}
.audit .arrows{padding-left:8px}
.aim{position:absolute;left:272px;top:38px;width:180px}
.amp{position:absolute;left:228px;top:30px;font-family:"Exo 2",sans-serif;font-size:52px;font-weight:600;color:#0a3e66;line-height:1}
.outcomes{left:13px;top:368px;width:487px;height:252px}
.outcomes .section-title{position:absolute;left:8px;top:8px}
.lessons{left:13px;top:655px;width:487px;height:347px;padding:8px 8px}
.lessons .lesson{margin-top:6px}
.lessons .lesson p{font-size:10.8px;line-height:16px}
.next{left:13px;top:1040px;width:487px;height:145px;padding:8px 10px}
.next ul{margin-top:6px;padding-left:12px}
.strategy{left:508px;top:163px;width:335px;height:909px}
.strategy .section-title{position:absolute;left:8px;top:8px}
.strategy .lead{position:absolute;left:9px;top:30px;font-size:10.3px}
.phase{position:absolute;left:0;width:335px}
.phase-label{position:absolute;left:10px;width:34px;writing-mode:vertical-rl;transform:rotate(180deg);font-family:"Exo 2",sans-serif;display:flex;flex-direction:column;align-items:center;justify-content:flex-start;white-space:nowrap}
.phase-label .year{font-size:17px;font-weight:600;letter-spacing:.5px;line-height:20px}
.phase-label .stage{font-size:9px;line-height:11px}
.phase-body{position:absolute;left:61px;top:0;width:266px}
.phase-body h4{font-size:10.3px;font-weight:400;line-height:16px;margin-top:6px}
.phase-body h4:first-child{margin-top:0}
.green{color:var(--green)}.orange{color:var(--orange)}.grey{color:var(--grey)}.yellow{color:var(--yellow)}.plum{color:var(--plum)}
.thanks{left:508px;top:1085px;width:335px;height:100px;padding:8px 12px}
.thanks p{line-height:16px}
.contact{position:absolute;right:12px;bottom:8px;font-size:10.3px}
.contact b{font-family:"Exo 2",sans-serif;color:var(--subhead);font-weight:500;font-size:12.5px}
.connector{position:absolute}
</style>
</head>
<body>
<header class="poster-header">
  <div class="author-note"><strong>Authors:</strong>Nora Halloway, Ines Marwood, &amp; Tom Aldridge</div>
  <h1 class="poster-title">
    <span class="name">CLEAR LEDGER:</span>
    <span class="line">an electronic interdisciplinary documentation</span>
    <span class="line">system for patient admissions and care planning</span>
  </h1>
</header>

<main class="field"></main>

<svg class="connector" style="left:0;top:150px" width="857" height="1050" aria-hidden="true">
  <g fill="#0b5688">
    <polygon points="470,78 492,78 492,68 512,90 492,112 492,102 470,102"/>
    <polygon points="505,315 488,315 488,305 468,327 488,349 488,339 505,339"/>
    <polygon points="231,470 251,470 251,484 262,484 241,504 220,484 231,484"/>
    <polygon points="231,852 251,852 251,866 262,866 241,886 220,866 231,866"/>
    <polygon points="470,964 492,964 492,954 512,976 492,998 492,988 470,988"/>
  </g>
</svg>

<section class="panel background">
  <h2 class="section-title">BACKGROUND <small>➔ the problems with paper needed a solution.</small></h2>
  <span class="amp" aria-hidden="true">&amp;</span>
  <div class="audit">
    <h3 class="sub">AUDIT</h3>
    <p>An audit of Westbrook Hospital's inpatient, paper-based documentation revealed:</p>
    <ul class="arrows">
      <li>Inconsistency in documentation practices</li>
      <li>Duplication of information</li>
      <li>Variable contributions to care planning and goal setting from team members</li>
      <li>Failure to meet documentation related targets</li>
    </ul>
  </div>
  <div class="aim">
    <h3 class="sub">AIM</h3>
    <p>The aim of the Clear Ledger project was to develop and integrate the use of an interdisciplinary electronic documentation system for all admissions, care planning, team meetings and handovers to address these problems</p>
  </div>
</section>

<section class="panel outcomes">
  <h2 class="section-title">OUTCOMES <small>➔ improvements after three months of Clear Ledger</small></h2>
</section>

<section class="panel lessons">
  <h2 class="section-title">LESSONS LEARNED <small>➔ What worked for Clear Ledger</small></h2>
  <div class="lesson"><p><span class="sub">CLINICAL ENGAGEMENT</span>&nbsp; Buy-in from clinician groups at both ward and management level was crucial to smooth transition during the change implementation process</p></div>
  <div class="lesson"><p><span class="sub">DEDICATED PROJECT SUPPORT AND COLLABORATION WITH REPRESENTATIVES OF ALL STAKEHOLDERS</span>&nbsp; Both the Working Group and Steering Committee combined the expertise of our business unit with stakeholder delegates to develop and deploy the product.</p></div>
  <div class="lesson"><p><span class="sub">TRAINING AND SUPPORT WITHIN THE CLINICAL ENVIRONMENT</span><br>Our project achieved this through up-skilling of designated champions, who continue to act as ward-based educational support for other staff and who promote Clear Ledger within their own ward and departments.</p></div>
  <div class="lesson"><p><span class="sub">IT RESOURCING AND UNDERSTANDING OF THE BUSINESS REQUIREMENT</span>&nbsp; Communication between the technical and clinical contributors to Clear Ledger allowed a collaborative approach and improved delivery of the product</p></div>
  <div class="lesson"><p><span class="sub">HARNESSING MOTIVATION</span>&nbsp; Good will and enthusiasm generated by Clear Ledger has been used to initiate and support related quality improvements</p></div>
</section>

<section class="panel next">
  <h2 class="section-title">NEXT STEPS</h2>
  <ul class="arrows">
    <li>Increases the scope of Clear Ledger to include other documents and progress notes</li>
    <li>Provision of faster speed of technology</li>
    <li>Extra-training for specific clinician subgroups and up-skilling to establish a second group of champions</li>
    <li>Review documents to improve flow through documentation to the discharge summary, clinical decision support, quality of care delivery and goal setting, data usage for research and audit efficiency</li>
  </ul>
</section>

<section class="panel strategy">
  <h2 class="section-title">STRATEGY FOR CHANGE <small>➔</small></h2>
  <p class="lead">develop and deploy an electronic package to improve patient care</p>

  <div class="phase" style="top:65px">
    <div class="phase-label green" style="top:-6px;height:112px"><span class="year">JULY 2011</span><span class="stage">Project Commissioned</span></div>
    <div class="phase-body">
      <h4>PEOPLE</h4>
      <p>Multidisciplinary Working Group: Clinicians, Project Management, and IT</p>
      <h4>PROCESSES</h4>
      <ul class="arrows"><li>Review of paper based documentation – areas to streamline and auto-populate identified</li><li>Design and testing of electronic versions</li></ul>
      <h4>MEASURES</h4>
      <p>All wards: Documentation Audit, Survey - Attitudes, Documentation Time – self report (individuals) and teams (time-motion)</p>
    </div>
  </div>

  <div class="phase" style="top:265px">
    <div class="phase-label orange" style="top:-4px;height:142px"><span class="year">NOVEMBER 2012</span><span class="stage">Project Commenced</span></div>
    <div class="phase-body">
      <h4>PEOPLE</h4>
      <p>Pilot Ward Staff (32 beds)</p>
      <h4>PROCESSES</h4>
      <ul class="arrows"><li>Pilot of Clear Ledger</li><li>On-ward training</li><li>Change requests to improve documents and fix bugs based on feedback</li></ul>
      <h4>MEASURES</h4>
      <ul class="arrows"><li>Feedback surveys, verbal log, on-site forms</li><li>Pilot ward: 3-month repeat all measures plus user satisfaction</li></ul>
    </div>
  </div>

  <div class="phase" style="top:462px">
    <div class="phase-label grey" style="top:-8px;height:156px"><span class="year">JUNE 2013</span><span class="stage">Preparation for site-wide roll-out</span></div>
    <div class="phase-body">
      <h4>PEOPLE</h4>
      <p>Steering Committee: Executive, project management, HIS, clinician leaders, IT representatives</p>
      <h4>PROCESSES</h4>
      <ul class="arrows"><li>Refine Clear Ledger based on feedback</li><li>Marketing and staff engagement: flyers, videos, forum presentations</li><li>Training: Champion users, all staff</li></ul>
      <h4>MEASURES</h4>
      <ul class="arrows"><li>Pilot ward: 9-month repeat all measures</li><li>Site: documentation time of work sampling</li></ul>
    </div>
  </div>

  <div class="phase" style="top:660px">
    <div class="phase-label yellow" style="top:-10px;height:138px"><span class="year">FEBRUARY 2014</span><span class="stage">Clear Ledger implemented</span></div>
    <div class="phase-body">
      <h4>PEOPLE</h4>
      <p>All staff across six remaining subacute wards</p>
      <h4>PROCESSES</h4>
      <ul class="arrows"><li>Staged roll-out to consecutive wards</li></ul>
      <h4>MEASURES</h4>
      <ul class="arrows"><li>Feedback via champions and ward management</li><li>Change requests logged for review at end implementation</li></ul>
    </div>
  </div>

  <div class="phase" style="top:807px">
    <div class="phase-label plum" style="top:-6px;height:94px"><span class="year">APRIL 2014</span><span class="stage">Roll-out completed</span></div>
    <div class="phase-body">
      <h4>MEASURES</h4>
      <p>Site: Three-month repeat documentation audit, survey, plus user satisfaction</p>
    </div>
  </div>
</section>

<section class="panel thanks">
  <h2 class="section-title">ACKNOWLEDGEMENTS</h2>
  <p>The Clear Ledger Steering Committee and Working Group<br>Westbrook Hospital Staff<br>Harbourline Health Information Technology Department</p>
  <p class="contact"><b>CONTACT:</b> ➔ nora.halloway@mailbox.net</p>
</section>
</body>
</html>
```